Quorvantelline.com

I need a site that I can sell dewatering equipment to the construction industry.
Ie, pipes fittings pumps and other such things needed to remove the groundwater on construction sites. Here in Florida, it’s needed almost everywhere seeing we are at sea level.
I want to be able to sell these products on the site and receive

Coded - Design and coding required

1 page

```html
<!DOCTYPE html>
<html lang="en">
<head>
<meta charset="utf-8">
<title>Quorvantelline</title>
<link rel="stylesheet" href="https://fonts.googleapis.com/css2?family=Ubuntu:wght@400;500;700&family=Open+Sans:wght@400;600&display=swap">
<style>
:root{
  --gold:#b8962e;
  --gold-light:#d4b24a;
  --dark:#333333;
  --darker:#2a2a2a;
  --ink:#222222;
  --muted:#555555;
  --field:#eeeeee;
  --white:#ffffff;
  --head:"Ubuntu",sans-serif;
  --body:"Open Sans",sans-serif;
}
*{box-sizing:border-box;margin:0;padding:0}
html,body{width:1200px;height:4018px;overflow:hidden}
body{position:relative;background:var(--white);font-family:var(--body);color:var(--ink)}
.abs{position:absolute}
.btn{position:absolute;height:28px;width:130px;border-radius:14px;background:var(--gold);color:var(--white);font:600 12px/28px var(--body);text-align:center}
.btn.light{background:var(--white);color:var(--gold)}
.section-title{position:absolute;left:0;width:1200px;text-align:center;font:400 28px var(--head);color:var(--ink)}
.arrows{position:absolute;display:flex;gap:6px}
.arrows span{width:16px;height:16px;border-radius:50%;border:1.5px solid #888;display:block}
.arrows span.on{background:var(--gold);border-color:var(--gold)}

/* header */
.site-header{position:absolute;left:0;top:0;width:1200px;height:102px;background:var(--white)}
.brand{position:absolute;left:118px;top:34px;display:flex;align-items:center;gap:10px;font:700 24px var(--head);color:var(--gold)}
.brand i{width:34px;height:34px;border-radius:50%;background:var(--gold);display:block}
.nav{position:absolute;left:502px;top:42px;display:flex;gap:28px;font:400 14px var(--body);color:var(--ink)}
.nav a{color:inherit;text-decoration:none}
.nav .active{color:var(--gold);position:relative}
.nav .active:after{content:"";position:absolute;left:0;right:0;top:-42px;height:3px;background:var(--gold)}
.tools{position:absolute;left:955px;top:40px;display:flex;gap:22px}

/* hero */
.hero{position:absolute;left:0;top:102px;width:1200px;height:628px;background:linear-gradient(180deg,#7d8a93 0%,#a0a8a5 40%,#6c6a58 70%,#8a7f66 100%)}
.hero-title{position:absolute;left:0;width:1200px;top:420px;text-align:center;font:500 38px var(--head);color:var(--white)}
.hero .slide-arrow{position:absolute;top:332px;width:26px;height:26px;border-radius:50%;background:var(--white)}
.dots{position:absolute;top:596px;left:570px;display:flex;gap:8px}
.dots i{width:8px;height:8px;border-radius:50%;background:var(--white);display:block}

/* products */
.product{position:absolute;top:935px;width:225px;height:351px;border:1px solid #dddddd;background:var(--white)}
.product .photo{position:absolute;left:14px;top:22px;width:195px;height:170px;background:linear-gradient(180deg,#f0f0f0,#d6c17a 60%,#444)}
.product h3{position:absolute;top:244px;width:100%;text-align:center;font:400 18px var(--head);color:var(--ink)}
.product p{position:absolute;top:284px;left:16px;right:16px;text-align:center;font:400 12px/17px var(--body);color:var(--muted)}
.product.active{border:3px solid var(--gold)}
.product.active .foot{position:absolute;left:0;right:0;bottom:0;height:130px;background:var(--gold)}
.product.active h3,.product.active p{color:var(--white)}

/* services */
.services{position:absolute;left:0;top:1455px;width:1200px;height:501px;background:var(--gold)}
.services .shade{position:absolute;left:75px;top:78px;width:455px;height:370px;background:#8c7124;opacity:.55}
.vertical-label{position:absolute;font:700 34px var(--head);color:rgba(255,255,255,.18);transform:rotate(-90deg);transform-origin:left top;white-space:nowrap}
.services .photo{position:absolute;left:131px;top:107px;width:464px;height:306px;background:linear-gradient(180deg,#c9ccd0,#e6e6e2 50%,#d4b43c 80%,#9a9a9a)}
.services h2{position:absolute;left:635px;top:98px;font:500 30px var(--head);color:var(--white)}
.services .rule{position:absolute;left:635px;top:140px;width:60px;height:2px;background:var(--white)}
.services p{position:absolute;left:635px;top:158px;width:445px;font:400 13px/19px var(--body);color:var(--white)}
.services ul{position:absolute;left:635px;top:226px;list-style:none;font:400 18px/34px var(--body);color:var(--white)}
.services li:before{content:"";display:inline-block;width:0;height:0;border-left:6px solid var(--white);border-top:5px solid transparent;border-bottom:5px solid transparent;margin-right:10px}

/* gallery */
.tile{position:absolute;background:linear-gradient(180deg,#a9b0ae,#6f7f5c 60%,#4e5c3a)}
.tile.big{background:linear-gradient(180deg,#b7bdbb 0%,#c4b25a 45%,#5b6d3a 100%)}

/* blogs */
.blogs{position:absolute;left:0;top:2661px;width:1200px;height:555px;background:var(--gold)}
.blogs h2{position:absolute;left:0;width:1200px;top:44px;text-align:center;font:400 30px var(--head);color:var(--white)}
.post{position:absolute;top:110px;width:311px;height:322px;background:var(--white)}
.post .photo{position:absolute;left:9px;top:9px;width:293px;height:180px;background:linear-gradient(135deg,#9aa0a6,#7a6f66 50%,#b44)}
.post h3{position:absolute;left:9px;top:198px;font:600 13px var(--body);color:var(--ink)}
.post .meta{position:absolute;left:9px;top:222px;width:293px;font:400 13px var(--body);color:var(--ink);display:flex;justify-content:space-between}
.post p{position:absolute;left:9px;top:246px;width:290px;font:400 13px/17px var(--body);color:var(--muted)}
.post .more{position:absolute;left:9px;top:288px;font:400 13px var(--body);color:var(--muted)}

/* contact */
.field{position:absolute;background:var(--field);font:400 11px var(--body);color:var(--muted);padding:8px 14px}

/* footer */
.site-footer{position:absolute;left:0;top:3591px;width:1200px;height:427px;background:var(--dark)}
.site-footer h4{position:absolute;top:126px;font:400 16px var(--head);color:var(--white)}
.site-footer .uline{position:absolute;top:152px;width:60px;height:2px;background:var(--white)}
.site-footer .txt{position:absolute;font:400 13px/17px var(--body);color:var(--white)}
.links{position:absolute;left:450px;top:208px;list-style:none;font:400 13px/19px var(--body);color:var(--white)}
.links li:before{content:"";display:inline-block;width:5px;height:5px;border-radius:50%;background:var(--white);margin-right:10px;vertical-align:middle}
.addr{position:absolute;left:630px;top:204px;font:400 13px/20px var(--body);color:var(--white)}
.subscribe{position:absolute;left:868px;top:258px;width:210px;height:24px;background:var(--white);font:400 11px/24px var(--body);color:var(--muted);padding-left:12px}
.subscribe b{position:absolute;right:0;top:0;width:36px;height:24px;background:var(--gold)}
.social{position:absolute;left:830px;top:3975px;display:flex;gap:14px}
.social i{width:30px;height:30px;border-radius:6px;display:block}
</style>
</head>
<body>

<header class="site-header">
  <div class="brand"><i></i>Quorvantelline</div>
  <nav class="nav">
    <a class="active">Home</a><a>About us</a><a>Product</a><a>Gallery</a><a>Blog</a><a>Contact us</a>
  </nav>
  <div class="tools">
    <svg width="16" height="16" viewBox="0 0 16 16"><path d="M8 14 2 8a3.2 3.2 0 0 1 6-3 3.2 3.2 0 0 1 6 3z" fill="none" stroke="#333" stroke-width="1.6"/></svg>
    <svg width="16" height="16" viewBox="0 0 16 16"><path d="M1 2h3l2 8h8l1-6H5" fill="none" stroke="#333" stroke-width="1.6"/><circle cx="7" cy="13.5" r="1.3" fill="#333"/><circle cx="13" cy="13.5" r="1.3" fill="#333"/></svg>
    <svg width="16" height="16" viewBox="0 0 16 16"><circle cx="7" cy="7" r="5" fill="none" stroke="#333" stroke-width="1.8"/><path d="m11 11 4 4" stroke="#333" stroke-width="2"/></svg>
    <svg width="16" height="16" viewBox="0 0 16 16"><path d="M1 3h14M1 8h14M1 13h14" stroke="#333" stroke-width="2"/></svg>
  </div>
</header>

<section class="hero" role="img" aria-label="Yellow trailer-mounted dewatering pump with hoses on a wet construction site">
  <div class="hero-title">Quorvantelline</div>
  <div class="btn" style="left:535px;top:382px">Read More</div>
  <div class="slide-arrow" style="left:52px"></div>
  <div class="slide-arrow" style="left:1123px"></div>
  <div class="dots"><i></i><i></i><i></i><i></i></div>
</section>
<svg class="abs" style="left:0;top:690px" width="1200" height="42" viewBox="0 0 1200 42" preserveAspectRatio="none">
  <path d="M0 42V24C300 4 700 4 1200 14V42Z" fill="var(--gold)"/>
  <path d="M0 42V32C320 14 720 12 1200 26V42Z" fill="#fff"/>
</svg>

<h2 class="section-title" style="top:833px">Feature Product</h2>
<div class="arrows" style="left:1038px;top:840px"><span></span><span class="on"></span></div>

<div class="product" style="left:120px"><div class="photo" role="img" aria-label="Yellow skid-mounted pump unit"></div><h3>Product Name</h3><p>Lorem Ipsum is simply dummy text gallery in the printing.</p></div>
<div class="product active" style="left:364px"><div class="foot"></div><div class="photo" role="img" aria-label="Yellow diesel pump set"></div><h3>Product Name</h3><p>Lorem Ipsum is simply dummy text gallery in the printing.</p></div>
<div class="product" style="left:611px"><div class="photo" role="img" aria-label="Orange engine-driven pump"></div><h3>Product Name</h3><p>Lorem Ipsum is simply dummy text gallery in the printing.</p></div>
<div class="product" style="left:855px"><div class="photo" role="img" aria-label="Slurry pump casing"></div><h3>Product Name</h3><p>Lorem Ipsum is simply dummy text gallery in the printing.</p></div>
<div class="btn" style="left:535px;top:1350px">View More</div>

<section class="services">
  <div class="shade"></div>
  <div class="vertical-label" style="left:86px;top:415px">Pumping Services</div>
  <div class="photo" role="img" aria-label="Yellow pumping equipment on a snowy site"></div>
  <h2>Our Services</h2>
  <div class="rule"></div>
  <p>Lorem Ipsum is simply dummy text in of the printing and typesetting industry. Lorem Ipsum has been the industry's standard dummy text ever since the 1500s.</p>
  <ul><li>Pumping Services</li><li>Dewatering</li><li>Water Filtration &amp; Treatment</li><li>Drilling</li></ul>
  <div class="btn light" style="left:635px;top:382px">Read More</div>
</section>

<h2 class="section-title" style="top:2022px">Our Gallery</h2>
<div class="vertical-label" style="left:1148px;top:2500px;color:rgba(0,0,0,.07);font-size:52px">Our Gallery</div>
<div class="tile big" style="left:120px;top:2088px;width:475px;height:407px" role="img" aria-label="Trailer pump beside a pond"></div>
<div class="tile" style="left:616px;top:2088px;width:220px;height:190px" role="img" aria-label="Worker setting up a pump"></div>
<div class="tile" style="left:858px;top:2088px;width:219px;height:190px" role="img" aria-label="Workers at a pump on site"></div>
<div class="tile" style="left:616px;top:2300px;width:220px;height:195px" role="img" aria-label="Pump in a muddy excavation"></div>
<div class="tile" style="left:858px;top:2300px;width:219px;height:195px" role="img" aria-label="Yellow generator units"></div>
<div class="btn" style="left:535px;top:2550px">View More</div>

<section class="blogs">
  <h2>Our Blogs</h2>
  <div class="arrows" style="left:1032px;top:50px"><span style="border-color:#fff"></span><span class="on" style="background:#fff;border-color:#fff"></span></div>
  <article class="post" style="left:110px"><div class="photo" role="img" aria-label="Red plug valve on a pipe"></div><h3>Industrial plug valve on the pipe</h3><div class="meta"><span>Jun 01, 2018</span><span>♡20 &nbsp; 12</span></div><p>Lorem Ipsum is simply dummy text of the matter and typesetting in industry.</p><div class="more">Read More</div></article>
  <article class="post" style="left:445px"><div class="photo" role="img" aria-label="Hand valve in an industrial plant"></div><h3>hand valve in industrial plant</h3><div class="meta"><span>Jun 02, 2018</span><span>♡20 &nbsp; 12</span></div><p>Lorem Ipsum is simply dummy text of the matter and typesetting in industry.</p><div class="more">Read More</div></article>
  <article class="post" style="left:777px"><div class="photo" role="img" aria-label="Stainless steel pipework"></div><h3>industry stainless pipe</h3><div class="meta"><span>Jun 10, 2018</span><span>♡20 &nbsp; 12</span></div><p>Lorem Ipsum is simply dummy text of the matter and typesetting in industry.</p><div class="more">Read More</div></article>
  <div class="btn light" style="left:535px;top:463px">View More</div>
</section>

<h2 class="section-title" style="top:3303px">Quick Contact</h2>
<svg class="abs" style="left:550px;top:3344px" width="100" height="10"><path d="M0 5h42M58 5h42" stroke="var(--gold)" stroke-width="1.5"/><circle cx="50" cy="5" r="4" fill="none" stroke="var(--gold)" stroke-width="1.5"/></svg>
<div class="field" style="left:247px;top:3369px;width:219px;height:29px">Name</div>
<div class="field" style="left:485px;top:3369px;width:217px;height:29px">Phone</div>
<div class="field" style="left:721px;top:3369px;width:220px;height:29px">Email</div>
<div class="field" style="left:247px;top:3412px;width:694px;height:88px">Message</div>
<div class="btn" style="left:535px;top:3537px">View More</div>

<svg class="abs" style="left:0;top:3568px" width="1200" height="50" viewBox="0 0 1200 50" preserveAspectRatio="none">
  <path d="M0 50V20C400 44 800 40 1200 0V50Z" fill="var(--gold)"/>
  <path d="M0 50V30C400 50 800 46 1200 12V50Z" fill="var(--dark)"/>
</svg>
<footer class="site-footer">
  <div class="brand" style="left:115px;top:126px;color:#fff;font-size:20px"><i style="width:28px;height:28px;background:#fff"></i>Quorvantelline</div>
  <div class="txt" style="left:118px;top:204px;width:250px">Lorem Ipsum is simply dummy text the printing and yprsetting industry. has been Lorem Ipsum is simply dummy text the Lorem Ipsum is simply dummy text the the industry's standard. dummy...</div>
  <h4 style="left:450px">Quick Link</h4><div class="uline" style="left:450px"></div>
  <ul class="links"><li>Home</li><li>About us</li><li>Product</li><li>Blog</li><li>Gallery</li><li>Contact us</li></ul>
  <h4 style="left:630px">Address</h4><div class="uline" style="left:630px"></div>
  <div class="addr">&#9679;&nbsp; 48 Marlowe Basin Road<br>&nbsp;&nbsp;&nbsp;&nbsp;Tressford, USA<br>&nbsp;&nbsp;&nbsp;&nbsp;Zip :5071<br>&#9742;&nbsp; +100 555 0192<br>&#9993;&nbsp; info@quorvantelline.com</div>
  <h4 style="left:868px">Subscribe Our Newsletter</h4><div class="uline" style="left:868px"></div>
  <div class="txt" style="left:868px;top:204px;width:220px">Lorem Ipsum is simply dummy and typesetting in industry.</div>
  <div class="subscribe">Email Here<b></b></div>
  <div class="abs" style="left:118px;top:360px;width:964px;height:1px;background:#666"></div>
  <div class="txt" style="left:118px;top:386px">Copyright © 2018 Quorvantelline. All Rights Reserved.</div>
</footer>
<div class="social"><i style="background:#3b5a9a"></i><i style="background:#9b3fa8"></i><i style="background:#3aa0d8"></i><i style="background:#2a78b0"></i><i style="background:#d0302a"></i></div>

</body>
</html>
```